We need a designer to help us represent our unique approach to creating lesson plans for digital learning. At the Autumn Gathering for Online Fluency, held in Providence RI this July 13 - 18, we'll use your design with 100 teachers and then put it online to reach hundreds of thousands more.

We have a draft visual of our model that we like - but it's not pretty (Since we are not designers, it looks a little clunky).

Please create a simple and attractive design in two versions: (1) one that we can use as a 1-page printed handout and (2) one that we can use where teachers can fill in sections and write ideas under each section of the graphic.

Why you should bid on this job? We're a leading provider of digital and media literacy curriculum resources with a huge international and national audience. Working with us will establish your expertise in the area of educational multimedia design.

Target Market(s)

Elementary and secondary teachers in public schools

Industry/Entity Type

Digital

Font styles to use
Sans Serif

Requirements
Must have
• TITLE : Digital Literacy Curriculum Framework

1 page version - suitable for use as a poster or 1-page flyer

Fillable form version - suitable for use as a handout with spaces for teachers to write

```html
<!DOCTYPE html>
<html lang="en">
<head>
<meta charset="utf-8">
<title>Digital Literacy Curriculum Framework</title>
<link rel="stylesheet" href="https://fonts.googleapis.com/css2?family=Arimo:wght@400;700&display=swap">
<style>
  :root {
    --page-bg: #e9e9e9;
    --ink: #111111;
    --frame: #0d0d0d;
    --label-light: #ffffff;
    --green: #4f9a2a;
    --green-dark: #2f6418;
    --red: #b42a22;
    --red-dark: #6e1510;
    --orange: #e79a1c;
    --orange-dark: #9b5e0a;
    --blue: #1f8fe0;
    --blue-dark: #0c4f8c;
    --purple: #b02ee0;
    --purple-dark: #6a1390;
    --hub: #d8d8d8;
    --hub-dark: #9a9a9a;
    --tile: #111111;
    --tile-icon-a: #29a8e0;
    --tile-icon-b: #7dc242;
  }
  * { margin: 0; padding: 0; box-sizing: border-box; }
  html, body { width: 900px; height: 1200px; overflow: hidden; }
  body {
    background: var(--page-bg);
    font-family: "Arimo", Arial, sans-serif;
    color: var(--ink);
    position: relative;
  }
  .framework-title {
    position: absolute;
    top: 100px;
    left: 0;
    width: 900px;
    text-align: center;
    font-size: 40px;
    font-weight: 400;
    letter-spacing: 0.2px;
  }
  .framework-diagram {
    position: absolute;
    top: 0;
    left: 0;
  }
  .corner-label {
    font-family: "Arimo", Arial, sans-serif;
    font-size: 34px;
    font-weight: 700;
    fill: var(--ink);
  }
  .piece-label {
    font-family: "Arimo", Arial, sans-serif;
    font-weight: 700;
    fill: var(--label-light);
  }
  .tile-label {
    font-family: "Arimo", Arial, sans-serif;
    font-size: 22px;
    font-weight: 700;
    fill: var(--label-light);
  }
  .task-label {
    font-family: "Arimo", Arial, sans-serif;
    font-size: 28px;
    fill: var(--ink);
  }
</style>
</head>
<body>
  <h1 class="framework-title">Digital Literacy Curriculum Framework</h1>

  <svg class="framework-diagram" width="900" height="1200" viewBox="0 0 900 1200" role="group" aria-label="Curriculum framework diagram">
    <defs>
      <radialGradient id="grad-green" cx="40%" cy="30%" r="75%">
        <stop offset="0" stop-color="#9fe06a"/><stop offset="1" stop-color="#4f9a2a"/>
      </radialGradient>
      <radialGradient id="grad-red" cx="40%" cy="30%" r="75%">
        <stop offset="0" stop-color="#e4574c"/><stop offset="1" stop-color="#b42a22"/>
      </radialGradient>
      <radialGradient id="grad-orange" cx="45%" cy="30%" r="75%">
        <stop offset="0" stop-color="#ffcf6a"/><stop offset="1" stop-color="#e79a1c"/>
      </radialGradient>
      <radialGradient id="grad-blue" cx="40%" cy="30%" r="75%">
        <stop offset="0" stop-color="#7fd0ff"/><stop offset="1" stop-color="#1f8fe0"/>
      </radialGradient>
      <radialGradient id="grad-purple" cx="50%" cy="30%" r="75%">
        <stop offset="0" stop-color="#e58cff"/><stop offset="1" stop-color="#b02ee0"/>
      </radialGradient>
      <radialGradient id="grad-hub" cx="50%" cy="35%" r="70%">
        <stop offset="0" stop-color="#ffffff"/><stop offset="1" stop-color="#d8d8d8"/>
      </radialGradient>
    </defs>

    <g class="outer-frame">
      <rect x="60" y="210" width="780" height="905" fill="none" stroke="var(--frame)" stroke-width="18"/>
      <text class="corner-label" x="74" y="254">Purpose</text>
      <text class="corner-label" text-anchor="end" x="826" y="254">Assessment</text>
      <text class="corner-label" x="74" y="1088">Content</text>
      <text class="corner-label" text-anchor="end" x="826" y="1088">Pedagogy</text>
    </g>

    <g class="piece piece-work-products">
      <ellipse cx="452" cy="332" rx="155" ry="88" fill="var(--green-dark)"/>
      <ellipse cx="452" cy="312" rx="155" ry="88" fill="url(#grad-green)"/>
      <text class="piece-label" font-size="30" text-anchor="middle" x="452" y="282">Work</text>
      <text class="piece-label" font-size="30" text-anchor="middle" x="452" y="316">Products</text>
    </g>
    <g class="piece piece-standards">
      <ellipse cx="200" cy="500" rx="175" ry="120" fill="var(--red-dark)"/>
      <ellipse cx="200" cy="474" rx="175" ry="120" fill="url(#grad-red)"/>
      <text class="piece-label" font-size="38" text-anchor="middle" transform="translate(160 490) rotate(-32)">Standards</text>
    </g>
    <g class="piece piece-instructional">
      <ellipse cx="718" cy="505" rx="165" ry="120" fill="var(--orange-dark)"/>
      <ellipse cx="718" cy="480" rx="165" ry="120" fill="url(#grad-orange)"/>
      <g transform="translate(790 446) rotate(40)">
        <text class="piece-label" font-size="26" text-anchor="middle" x="0" y="0">Instructional</text>
        <text class="piece-label" font-size="26" text-anchor="middle" x="0" y="32">Strategies</text>
      </g>
    </g>

    <g class="piece piece-texts">
      <ellipse cx="245" cy="855" rx="205" ry="160" fill="var(--blue-dark)"/>
      <ellipse cx="245" cy="822" rx="205" ry="160" fill="url(#grad-blue)"/>
      <text class="piece-label" font-size="50" text-anchor="middle" transform="translate(240 830) rotate(-32)">Texts</text>
    </g>
    <g class="piece piece-tools">
      <ellipse cx="672" cy="855" rx="200" ry="160" fill="var(--purple-dark)"/>
      <ellipse cx="672" cy="822" rx="200" ry="160" fill="url(#grad-purple)"/>
      <text class="piece-label" font-size="50" text-anchor="middle" transform="translate(690 850) rotate(40)">Tools</text>
    </g>

    <g class="hub">
      <ellipse cx="452" cy="538" rx="175" ry="148" fill="var(--hub-dark)"/>
      <ellipse cx="452" cy="516" rx="175" ry="148" fill="url(#grad-hub)"/>
      <rect x="376" y="462" width="152" height="90" fill="#f4f4f4" stroke="#555" stroke-width="2"/>
      <text class="task-label" text-anchor="middle" x="452" y="500">Task or</text>
      <text class="task-label" text-anchor="middle" x="452" y="536">Activity</text>
    </g>

    <g class="hub-tile tile-learners">
      <rect x="392" y="340" width="122" height="76" rx="6" fill="var(--tile)"/>
      <text class="tile-label" text-anchor="middle" x="453" y="368">Learners</text>
      <rect x="418" y="380" width="26" height="28" fill="var(--tile-icon-a)"/>
      <rect x="462" y="380" width="26" height="28" fill="var(--tile-icon-b)"/>
    </g>
    <g class="hub-tile tile-self">
      <rect x="256" y="432" width="84" height="84" rx="6" fill="var(--tile)"/>
      <text class="tile-label" text-anchor="middle" x="298" y="462">Self</text>
      <rect x="270" y="476" width="22" height="26" fill="var(--tile-icon-a)"/>
      <rect x="304" y="476" width="22" height="26" fill="var(--tile-icon-b)"/>
    </g>
    <g class="hub-tile tile-community">
      <rect x="558" y="428" width="134" height="92" rx="6" fill="var(--tile)"/>
      <text class="tile-label" text-anchor="middle" x="625" y="458">Community</text>
      <circle cx="625" cy="490" r="18" fill="none" stroke="var(--tile-icon-b)" stroke-width="5"/>
    </g>
    <g class="hub-tile tile-context">
      <rect x="396" y="590" width="114" height="84" rx="6" fill="var(--tile)"/>
      <text class="tile-label" text-anchor="middle" x="453" y="620">Context</text>
      <rect x="440" y="632" width="26" height="32" fill="var(--tile-icon-b)"/>
    </g>
  </svg>
</body>
</html>
```